eBook opt in for website

I write short ebooks (2500 words) to give free as an opt in. I need a cover design with block headers within the pages to highlight the specifics sections for PDF.
Book Title:
Bridgeway Mentoring
Sharpen Your Crew Guidance Using Five Simple Habits
I would like to see a design for the front cover that would emphasize a leader's personal growth to team.
The color that comes to mind is blue.
I do have a Brand Design and Icon if you need it.

Leaders with Team Responsibility
Business Consultant

```html
<!DOCTYPE html>
<html lang="en">
<head>
<meta charset="UTF-8">
<title>Bridgeway Mentoring – eBook Cover</title>
<link rel="stylesheet" href="https://fonts.googleapis.com/css2?family=Anton&family=Open+Sans:wght@600;700&display=swap">
<style>
  :root {
    --backdrop: #c9d8dd;
    --sky-top: #d6e6f0;
    --sky-bottom: #f4f7f8;
    --title-blue: #1e9bd6;
    --band-blue: #1a96cc;
    --white: #ffffff;
    --wood-light: #f0b868;
    --wood-mid: #d98f3a;
    --wood-deep: #9a5a1e;
    --badge-red: #8b2e2e;
  }
  * { box-sizing: border-box; margin: 0; padding: 0; }
  html, body {
    width: 1200px;
    height: 1200px;
    overflow: hidden;
    background: var(--backdrop);
  }
  .canvas {
    position: relative;
    width: 1200px;
    height: 1200px;
  }
  .cover {
    position: absolute;
    left: 252px;
    top: 60px;
    width: 696px;
    height: 1080px;
    overflow: hidden;
    background: linear-gradient(180deg, var(--sky-top) 0%, var(--sky-bottom) 32%);
    box-shadow: 0 18px 40px rgba(40, 60, 70, 0.25);
  }
  .cover-photo {
    position: absolute;
    left: 0;
    right: 0;
    top: 300px;
    bottom: 0;
    background:
      radial-gradient(circle at 48% 42%, #f4e9c8 0 5%, var(--wood-light) 14%, var(--wood-mid) 45%, var(--wood-deep) 100%);
    clip-path: polygon(0 12%, 40% 0, 60% 6%, 100% 0, 100% 100%, 0 100%);
  }
  .author-badge {
    position: absolute;
    left: 36px;
    top: 52px;
    width: 170px;
    height: 170px;
    border: 2px solid var(--badge-red);
    border-radius: 50%;
    display: flex;
    align-items: center;
    justify-content: center;
    text-align: center;
  }
  .author-badge__name {
    font-family: "Open Sans", sans-serif;
    font-weight: 700;
    font-size: 22px;
    line-height: 1.15;
    color: var(--badge-red);
  }
  .cover-title {
    position: absolute;
    right: 26px;
    top: 30px;
    text-align: right;
    font-family: "Anton", sans-serif;
    font-weight: 400;
    font-size: 104px;
    line-height: 0.98;
    color: var(--title-blue);
    -webkit-text-stroke: 2px var(--white);
    text-shadow: 3px 4px 6px rgba(0, 0, 0, 0.35);
    letter-spacing: 0.5px;
  }
  .subtitle-band {
    position: absolute;
    left: 0;
    right: 0;
    top: 770px;
    height: 160px;
    background: var(--band-blue);
    display: flex;
    align-items: center;
    padding: 0 40px 0 62px;
  }
  .subtitle {
    font-family: "Open Sans", sans-serif;
    font-weight: 700;
    color: var(--white);
    font-size: 30px;
    line-height: 1.3;
  }
  .subtitle__lead {
    font-size: 40px;
  }
</style>
</head>
<body>
  <main class="canvas">
    <section class="cover">
      <div class="cover-photo" role="img" aria-label="Top-down photograph of a square wooden spiral staircase with white railings"></div>
      <div class="author-badge">
        <span class="author-badge__name">Maren<br>Holloway</span>
      </div>
      <h1 class="cover-title">Bridgeway<br>Mentoring</h1>
      <div class="subtitle-band">
        <p class="subtitle">Sharpen Your <span class="subtitle__lead">Crew Guidance</span><br>Using Five Simple Habits</p>
      </div>
    </section>
  </main>
</body>
</html>
```